PowerPoint Design Project

I am looking to create a unique elegant, professional powerpoint for my events menus.

I have the menus, and the pricing and was looking to drop in each menu into a slide or two with some added stock photos where appropriate, but not needed everywhere.

There are nine menu, and some three four and five courses, so layout can and will vary.

looking for a way to insert them into a series of 18 or 20 slides, with a nice professional catered event setting, no photography specific to the event space, a focus on elegant food, wine, champagne accents can be incorporated.

it is essentially a catering brochure for an upscale caterer.
The Color Orange can be used for headers and Dark Brown upscale fonts

Target Market(s)

Corporate offices and Upscale Leisure Catering Events ( more Leisure elegant reception concepts vs strict cold corporate feel)

Industry/Entity Type

Catering

Requirements
Must have
• each slide should have a section for
Appetizer
soup
salad
entree
dessert
Nice to have
• more elegant, simple to read
boutique hotel so it can have a bit of character
Should not have
• cartoons, less than professional elements like bright color combos, to more elegant the better we have a brown and orange theme through the corporation

```html
<!DOCTYPE html>
<html lang="en">
<head>
<meta charset="utf-8">
<title>Californian Menu</title>
<link rel="stylesheet" href="https://fonts.googleapis.com/css2?family=EB+Garamond:wght@400;500&family=Jost:wght@300;400;600&display=swap">
<style>
  :root {
    --bg: #ffffff;
    --heading: #5a4646;
    --text: #6a5855;
    --band: #675252;
    --band-text: #f4efee;
    --accent: #f0922e;
  }
  * { margin: 0; padding: 0; box-sizing: border-box; }
  html, body { width: 1200px; height: 900px; overflow: hidden; background: var(--bg); }
  .slide { position: relative; width: 1200px; height: 900px; }
  .menu-section {
    position: absolute;
    right: 503px;
    text-align: right;
  }
  .section-entrees { top: 72px; }
  .section-accompaniments { top: 472px; }
  .section-title {
    font-family: "Jost", sans-serif;
    font-weight: 600;
    font-variant: small-caps;
    font-size: 35px;
    letter-spacing: 2px;
    line-height: 40px;
    color: var(--heading);
    margin-bottom: 16px;
  }
  .section-accompaniments .section-title { margin-bottom: 14px; }
  .menu-list { list-style: none; }
  .menu-list li {
    font-family: "EB Garamond", serif;
    font-size: 21px;
    line-height: 38px;
    color: var(--text);
    white-space: nowrap;
    letter-spacing: -0.2px;
  }
  .menu-list .choose { font-size: 20px; }
  .menu-name-band {
    position: absolute;
    left: 795px;
    top: 754px;
    width: 405px;
    height: 73px;
    background: var(--band);
    display: flex;
    align-items: center;
    padding-left: 14px;
  }
  .menu-name {
    font-family: "Jost", sans-serif;
    font-weight: 300;
    font-size: 32px;
    letter-spacing: 2.5px;
    color: var(--band-text);
    text-transform: uppercase;
  }
  .menu-name .initial { color: var(--accent); font-size: 38px; }
</style>
</head>
<body>
<main class="slide">
  <section class="menu-section section-entrees">
    <h2 class="section-title">Entrées</h2>
    <ul class="menu-list">
      <li class="choose">{choose 2}</li>
      <li>Pan Seared Salmon with Pinot Noir Red Onion Marmalade</li>
      <li>Grilled Chicken Breast with whole grain mustard sauce</li>
      <li>Cabernet Marinated Strip Loin with Red Onion and Fresh Thyme</li>
      <li>Stuffed Pork Loin with Apple Cranberry Sauce</li>
      <li>Marinated Short Ribs</li>
      <li>Peppered Skirt Steak</li>
      <li>Halibut with Red Pepper Nage</li>
    </ul>
  </section>

  <section class="menu-section section-accompaniments">
    <h2 class="section-title">Accompaniments</h2>
    <ul class="menu-list">
      <li class="choose">{choose 2}</li>
      <li>Grilled Medley of Country Vegetables</li>
      <li>Crispy Truffle Polenta</li>
      <li>Roasted Root Vegetables</li>
      <li>Creamed Summer Corn</li>
      <li>Grilled Artichokes</li>
      <li>Leek Bread Pudding</li>
    </ul>
  </section>

  <div class="menu-name-band">
    <h1 class="menu-name"><span class="initial">C</span>alifornian</h1>
  </div>
</main>
</body>
</html>
```